Gourmet food company looking for a dazzling label for their premuim vinagrette dressings

Need a food label that will dazzle our customer and prove what a premium product we have. We make high end gourmet dressing for vegetables, fruit, meat, poultry and fish.

Our label will fit on a 250 mil Tolvenka Square bottle. Labels should be a 4x5 or even 5x5 depending on the design. Nutritionals, bar codes and company blurb will be supplied later. We really want to test you all's talent on this one and are very excited to see your renderings!

Our dressings are Champagne Pear Vinaigrette, White Balsmic Vinaigrette, Mojito Lime Vinaigrette, Creamy-Avacado Lime Vinaigrette, and Asian Sesame Vinaigrette. I hope these names will help you envision our product and kinda what we are looking for.
Updates

Thank you all so far for your renderings.I really don't want pictures if that helps. Our logo can be smaller and/or the name of the product bigger. Perhaps we can even redesign Velora and remove the leaf as I don't really care for what I see yet.So good luck and thanks Added Friday, August 19, 2016

I am still looking for that clean - elegant design for our product as our product is just that. If you look on the internet at vinegars and oils you will see many designs that are simple yet elegant. Creative lettering, bordering, color (can be black and white) and size will help accomplish this. So I invite you to use all your creativity and help me find just what we need.Many thanks Added Tuesday, August 23, 2016

Project Deadline Extended Reason: So many great designs coming in that I wanted a few extra days to tweek!Great job all Added Friday, August 26, 2016

Project Deadline Extended Reason: Very good designs thus far. We just need a few more days.Thanks Added Wednesday, August 31, 2016

Target Market(s)

High end grocery and specialty stores.

Our side panel on the label will say "At Velora we're fanatics for great flavors and are passionate about finding the best ingredients. From simple to elegant our products are "simply velora".

Industry/Entity Type

It Company

Font styles to use
Serif
Decorative
Script

Requirements
Must have
• A label that will draw the consumer to pick it up! Need something bold and elegant...
Nice to have
• Again, I really would like to have a label that pops. Since the bottle front is only about 2inches in width it will need some creativity. Would like something very simple and elegant.
• If the designer does not like the logo, please feel free to design without it!
Should not have
• Dark dark colors. We are selling dressing and we don't want any colors that may distort the contents.
• No stock photos for the front. I don't want our dressing to look like the others on the self. Brambleth Kitchen just uses lettering and a their packaging is eye catching

```html
<!DOCTYPE html>
<html lang="en">
<head>
<meta charset="utf-8">
<title>Velora – Asian Sesame Vinaigrette Label</title>
<link href="https://fonts.googleapis.com/css2?family=Pinyon+Script&family=Cinzel+Decorative:wght@700&family=Alegreya+Sans:wght@400&display=swap" rel="stylesheet">
<style>
  :root {
    --page: #ffffff;
    --label-black: #0a0a0b;
    --ink: #f2f2f2;
    --silver-light: #f4f4f4;
    --silver-mid: #b8b8bc;
    --silver-dark: #6c6c72;
  }
  * { margin: 0; padding: 0; box-sizing: border-box; }
  html, body { width: 960px; height: 1200px; overflow: hidden; background: var(--page); }
  .canvas { position: relative; width: 960px; height: 1200px; }
  .label-shape { position: absolute; left: 0; top: 0; }
  .script { font-family: "Pinyon Script", cursive; color: var(--ink); }
  .body { font-family: "Alegreya Sans", sans-serif; color: var(--ink); }
  .block { position: absolute; text-align: center; }

  .ingredients { left: 26px; top: 248px; width: 200px; }
  .ingredients h2, .instructions h2, .nutritionals h2 { font-weight: 400; font-size: 25px; line-height: 1; }
  .ingredients p { font-size: 14px; line-height: 20px; margin-top: 6px; }

  .nutritionals { left: 26px; top: 440px; width: 200px; }
  .nutri-table { position: absolute; left: 22px; top: 46px; width: 180px; border-collapse: collapse; font-size: 13.5px; }
  .nutri-table td { height: 28.6px; padding: 0; text-align: left; }
  .nutri-table td.value { padding-left: 12px; border-left: 1px solid var(--ink); }
  .nutri-table td.name { width: 85px; }

  .brand { left: 260px; top: 234px; width: 440px; }
  .brand h1 { font-weight: 400; font-size: 56px; line-height: 1; }
  .brand p { font-size: 24px; margin-top: 6px; }

  .product-name { left: 240px; top: 502px; width: 480px; font-family: "Cinzel Decorative", serif; font-weight: 700; color: var(--ink); font-size: 38px; line-height: 60px; letter-spacing: 1px; }

  .instructions { left: 740px; top: 248px; width: 200px; }
  .instructions p { font-size: 13.6px; line-height: 20px; margin-top: 8px; }

  .company { left: 730px; top: 496px; width: 220px; }
  .company h3 { font-weight: 400; font-size: 20px; line-height: 1; }
  .company p { font-size: 13.6px; line-height: 20px; margin-top: 4px; }

  .contact { left: 740px; top: 714px; width: 200px; font-size: 10.5px; line-height: 18px; }
  .storage { left: 730px; top: 780px; width: 220px; font-size: 15px; }

  .badge-row { position: absolute; left: 742px; top: 810px; }
  .blank-panel { position: absolute; left: 741px; top: 861px; width: 189px; height: 89px; background: var(--page); }

  .brand-mark { position: absolute; left: 42px; top: 896px; }
  .brand-mark .name { font-family: "Alegreya Sans", sans-serif; font-size: 36px; color: var(--ink); line-height: 1; }
  .brand-mark .tag { font-family: "Alegreya Sans", sans-serif; font-size: 9.6px; color: var(--ink); margin-top: 2px; }

  .volume { left: 380px; top: 944px; width: 200px; font-size: 24px; }
</style>
</head>
<body>
<div class="canvas">
  <svg class="label-shape" width="960" height="1200" viewBox="0 0 960 1200" aria-hidden="true">
    <defs>
      <linearGradient id="silver" x1="0" y1="0" x2="1" y2="1">
        <stop offset="0" stop-color="var(--silver-light)"/>
        <stop offset="0.45" stop-color="var(--silver-dark)"/>
        <stop offset="0.7" stop-color="var(--silver-light)"/>
        <stop offset="1" stop-color="var(--silver-mid)"/>
      </linearGradient>
      <radialGradient id="plaque-glow" cx="0.5" cy="0.55" r="0.6">
        <stop offset="0" stop-color="#2a2a2d"/>
        <stop offset="1" stop-color="var(--label-black)"/>
      </radialGradient>
    </defs>
    <path class="label-body" d="M6,188 H300 C338,188 342,128 400,128 H560 C618,128 622,188 660,188 H954 V1020 H660 C622,1020 618,1080 560,1080 H400 C342,1080 338,1020 300,1020 H6 Z"
          fill="var(--label-black)" stroke="url(#silver)" stroke-width="4"/>
    <path class="plaque-frame" d="M274,500 H370 C392,500 398,460 480,460 C562,460 568,500 590,500 H686 V540 C704,540 720,560 720,602 C720,644 704,664 686,664 V700 H590 C568,700 562,744 480,744 C398,744 392,700 370,700 H274 V664 C256,664 240,644 240,602 C240,560 256,540 274,540 Z"
          fill="url(#silver)"/>
    <path class="plaque-inner" d="M282,507 H372 C396,507 404,468 480,468 C556,468 564,507 588,507 H678 V546 C698,546 711,566 711,602 C711,638 698,658 678,658 V693 H588 C564,693 556,736 480,736 C404,736 396,693 372,693 H282 V658 C262,658 249,638 249,602 C249,566 262,546 282,546 Z"
          fill="url(#plaque-glow)"/>
    <path class="plaque-dots" d="M290,514 H376 C400,514 408,476 480,476 C552,476 560,514 584,514 H670 V553 C690,553 702,572 702,602 C702,632 690,651 670,651 V686 H584 C560,686 552,728 480,728 C408,728 400,686 376,686 H290 V651 C270,651 258,632 258,602 C258,572 270,553 290,553 Z"
          fill="none" stroke="var(--ink)" stroke-width="2" stroke-dasharray="0 7" stroke-linecap="round"/>
  </svg>

  <section class="block ingredients">
    <h2 class="script">Ingredients</h2>
    <p class="body">Ingredients goes here<br>Ingredients 02 goes here,<br>Ingredients 03 goes here,<br>Ingredients 04.</p>
  </section>

  <section class="block nutritionals">
    <h2 class="script">Nutritionals</h2>
    <table class="nutri-table body">
      <tr><td class="name">Nutritionals</td><td class="value">00 oz</td></tr>
      <tr><td class="name">Nutritionals</td><td class="value">00 oz</td></tr>
      <tr><td class="name">Nutritionals</td><td class="value">00 oz</td></tr>
      <tr><td class="name">Nutritionals</td><td class="value">00 oz</td></tr>
      <tr><td class="name">Nutritionals</td><td class="value">00 oz</td></tr>
      <tr><td class="name">Nutritionals</td><td class="value">00 oz</td></tr>
    </table>
  </section>

  <header class="block brand script">
    <h1>Velora</h1>
    <p>Finely Crafted Gourmet Dressing</p>
  </header>

  <div class="block product-name">Asian<br>Sesame<br>Vinaigrette</div>

  <section class="block instructions">
    <h2 class="script">Instructions</h2>
    <p class="body">Lorem Ipsum is simply dummy<br>text of the printing and<br>typesetting industry. Lorem<br>Ipsum has been the industry's<br>standard dummy text ever since<br>the 1500s, when an unknown<br>printer took a galley of type and<br>scrambled it to make a type<br>specimen book.</p>
  </section>

  <section class="block company">
    <h3 class="script">Fairlow Provisions Ltd.</h3>
    <p class="body">412 Orrin Lane, 2nd Floor |<br>Halden Falls, 00000</p>
  </section>

  <div class="block contact body">www.velora-fine.com<br>hello@velora-fine.com<br>(000) 000 000</div>
  <div class="block storage script">Store in a cold and dark place</div>

  <svg class="badge-row" width="200" height="46" viewBox="0 0 200 46" aria-hidden="true">
    <circle cx="22" cy="23" r="19" fill="none" stroke="var(--silver-mid)" stroke-width="4"/>
    <circle cx="70" cy="23" r="19" fill="var(--silver-mid)"/>
    <circle cx="118" cy="23" r="20" fill="var(--silver-light)"/>
    <circle cx="118" cy="23" r="15" fill="var(--silver-dark)"/>
    <path d="M168,44 C156,40 154,28 162,18 C162,26 166,28 168,28 C166,18 172,8 178,2 C178,14 188,20 186,32 C184,40 178,44 168,44 Z" fill="var(--silver-mid)"/>
  </svg>
  <div class="blank-panel"></div>

  <div class="brand-mark">
    <div class="name">Velora</div>
    <div class="tag">Finely Crafted Gourmet Dressing</div>
  </div>

  <div class="block volume script">250 ml</div>
</div>
</body>
</html>
```